Private Practice Dietitian's Business Card

A 2-sided business card for a dietitian (medical nutritionist) in private practice within a natural therapies allied health clinic. The business card needs to imply warmth and professionalism.
Target Market(s)
Doctors who may refer patients to a dietitian and patients themselves who may request dietetic assessment, education and counselling.
Industry/Entity Type
Business
Requirements
Must have
- The business card must be an intense blue on the front at the bottom, gradually lightening towards the top of the card. Please see:
http://pinboardly.example/rupert_halvane/card-ideas/
for an example from "The quiet of the riverbank" book. I'd like an apple tree on the left with a pale silver/grey trunk (like the silver in the book cover)and branches that bends over to the right above the writing. Apples to be a turquoise/aqua colour similar to that in "The quiet of the riverbank" book cover. Front cover writing to read:
foodsteps
0462 883 917
foodsteps@kelvanet.example
'foodsteps' is one word but I would like the 'my' in turquoise/aqua to match the apples and the 'dietitian' and the phone number and email address in the pale silver/grey to match the tree trunk.
I'd like the foodsteps in larger font than the phone number and email address but for all 3 lines of text on the front of the business card to be stretched so they have the same left and right margin. (I hope this makes sense!)
I would like the back of the card to be white and the top section of text to be in the same turquoise/aqua from the apples on the front of the card and to read:
MAREE TOLVIN
Accredited Practising Dietitian (APD)
Bachelor of Health Science (Nutrition & Dietetics) - Honours
Master of Nutrition & Dietetics
This text should be stretched/compacted so that it all has the same left and right margin.
After this text there should be a blank line for spacing before the next section of text, which is to be in the silver/grey of the tree trunk. It should read:
Weight management
Diabetes
Impaired fasting glycaemia
Impaired glucose tolerance
Gestational diabetes
Wellness & general nutrition
Cardiovascular disease
high blood pressure
High cholesterol
High triglycerides
Fatty liver
Constipation
Diverticular disease
Coeliac disease
Irritable bowel syndrome
Gastroesophageal reflux
Lactose intolerance
Gout
Polycystic ovarian syndrome
Fertility
Pregnancy
Breastfeeding
Osteoporosis
Iron deficiency
Vegetarian eating
This set of text can run across the page from left to right and each medical condition could be separated from the next in some way to help with ease of reading. For example perhaps a space, dot and another space could separate the medical conditions. This set of text should be stretched so that the left and right margins of each line is the same. Thank you!
Nice to have
- An easy-to read but 'elegant' font would be nice - but I have no idea which one! Nothing too ornate, but not dull standard Times New Roman/Arial/Comic Sans either!
Should not have
- Times new roman/comic sans/arial fonts

```html
<!DOCTYPE html>
<html lang="en">
<head>
<meta charset="utf-8">
<title>foodsteps – Business Card</title>
<link href="https://fonts.googleapis.com/css2?family=Lato:wght@400;700;900&display=swap" rel="stylesheet">
<style>
  :root {
    --paper: #ffffff;
    --edge: #b9b9c2;
    --silver-ink: #64676f;
    --turquoise-deep: #127f95;
    --turquoise: #1f9bb3;
    --navy-deep: #15134d;
    --navy: #24206a;
    --royal: #2f3fae;
    --sky: #5a86d6;
    --emblem: #221d5c;
    --emblem-ring: #e8e8f2;
    --silver: #e6e8f0;
  }
  html, body {
    margin: 0;
    padding: 0;
    width: 1200px;
    height: 746px;
    overflow: hidden;
    background: var(--paper);
  }
  .sheet {
    position: relative;
    width: 1200px;
    height: 746px;
    font-family: 'Lato', sans-serif;
  }

  /* ---------- Back: services list ---------- */
  .card-services {
    position: absolute;
    left: 20px;
    top: 22px;
    width: 584px;
    height: 346px;
    box-sizing: border-box;
    border: 2px solid var(--edge);
    border-right: none;
    border-radius: 22px 0 0 22px;
    background: var(--paper);
  }
  .services-list {
    position: absolute;
    left: 0;
    right: 0;
    top: 56px;
    margin: 0;
    padding: 0;
    list-style: none;
    text-align: center;
    color: var(--silver-ink);
    font-size: 14.5px;
    letter-spacing: 2.4px;
    line-height: 22.3px;
  }
  .services-list b { font-weight: 900; color: #4c4f57; }

  /* ---------- Front: brand panel ---------- */
  .card-front {
    position: absolute;
    left: 604px;
    top: 22px;
    width: 562px;
    height: 346px;
    overflow: hidden;
    border-radius: 0 40px 40px 0 / 0 170px 170px 0;
    background: linear-gradient(180deg,
      var(--navy-deep) 0%,
      var(--navy) 28%,
      var(--royal) 40%,
      var(--sky) 52%,
      var(--royal) 64%,
      var(--navy) 78%,
      var(--royal) 100%);
  }
  .front-emblem {
    position: absolute;
    left: 22px;
    top: 73px;
    width: 200px;
    height: 200px;
  }
  .front-contact {
    position: absolute;
    left: 250px;
    top: 118px;
    width: 270px;
    text-align: center;
    color: var(--silver);
  }
  .front-wordmark {
    margin: 0 0 6px;
    font-size: 56px;
    line-height: 64px;
    font-weight: 400;
    letter-spacing: 1px;
  }
  .front-contact p.line {
    margin: 0;
    font-size: 15px;
    line-height: 22px;
  }
  .front-contact .phone { letter-spacing: 6.2px; }
  .front-contact .email { letter-spacing: 0.6px; }

  /* ---------- Back: practitioner details ---------- */
  .card-details {
    position: absolute;
    left: 50px;
    top: 372px;
    width: 548px;
    height: 346px;
    box-sizing: border-box;
    border: 2px solid var(--edge);
    border-radius: 22px 0 0 22px;
    overflow: hidden;
    background: var(--paper);
  }
  .credentials {
    position: absolute;
    left: 200px;
    right: 0;
    top: 22px;
    text-align: center;
    color: var(--turquoise);
  }
  .credentials .name {
    margin: 0 0 6px;
    font-size: 19px;
    font-weight: 900;
    letter-spacing: 1px;
    color: var(--turquoise-deep);
  }
  .credentials p {
    margin: 0;
    font-size: 16px;
    line-height: 22px;
    letter-spacing: 0.6px;
  }
  .credentials .spread { letter-spacing: 2px; }
  .details-band {
    position: absolute;
    left: 0;
    right: 0;
    top: 172px;
    height: 92px;
    background: linear-gradient(180deg,
      var(--royal) 0%,
      var(--sky) 22%,
      #2a54c4 45%,
      var(--royal) 70%,
      var(--navy) 100%);
  }
  .details-emblem {
    position: absolute;
    left: 24px;
    top: 118px;
    width: 200px;
    height: 200px;
  }
  .details-wordmark {
    position: absolute;
    left: 250px;
    top: 186px;
    margin: 0;
    font-size: 52px;
    line-height: 60px;
    font-weight: 400;
    letter-spacing: 1px;
    color: var(--silver);
  }
</style>
</head>
<body>
<main class="sheet">

  <section class="card-services" aria-label="Card back – services">
    <ul class="services-list">
      <li><b>W</b>eight management <b>D</b>iabetes</li>
      <li><b>I</b>mpaired fasting glycaemia</li>
      <li><b>I</b>mpaired glucose tolerance</li>
      <li><b>G</b>estational diabetes <b>W</b>ellness &amp; general nutrition</li>
      <li><b>C</b>ardiovascular disease <b>H</b>igh blood pressure</li>
      <li><b>H</b>igh cholesterol <b>H</b>igh triglycerides</li>
      <li><b>F</b>atty liver <b>C</b>onstipation <b>D</b>iverticular disease</li>
      <li><b>C</b>oeliac disease <b>I</b>rritable bowel syndrome</li>
      <li><b>G</b>astroesophageal reflux <b>L</b>actose intolerance</li>
      <li><b>G</b>out <b>P</b>olycystic ovarian syndrome <b>F</b>ertility</li>
      <li><b>P</b>regnancy <b>B</b>reastfeeding <b>O</b>steoporosis</li>
      <li><b>I</b>ron deficiency <b>V</b>egetarian eating</li>
    </ul>
  </section>

  <section class="card-front" aria-label="Card front – brand">
    <svg class="front-emblem" viewBox="0 0 200 200" aria-hidden="true">
      <circle cx="100" cy="100" r="97" fill="var(--emblem)" stroke="var(--emblem-ring)" stroke-width="3"/>
    </svg>
    <div class="front-contact">
      <p class="front-wordmark">foodsteps</p>
      <p class="line phone">0462 883 917</p>
      <p class="line email">foodsteps@kelvanet.example</p>
    </div>
  </section>

  <section class="card-details" aria-label="Card back – practitioner details">
    <div class="credentials">
      <h1 class="name">MAREE TOLVIN</h1>
      <p>Accredited Practising Dietitian (APD)</p>
      <p class="spread">Bachelor of Health Science</p>
      <p class="spread">(Nutrition &amp; Dietetics) - Honours</p>
      <p>Master of Nutrition &amp; Dietetics</p>
    </div>
    <div class="details-band"></div>
    <svg class="details-emblem" viewBox="0 0 200 200" aria-hidden="true">
      <circle cx="100" cy="100" r="97" fill="var(--emblem)" stroke="var(--emblem-ring)" stroke-width="3"/>
    </svg>
    <p class="details-wordmark">foodsteps</p>
  </section>

</main>
</body>
</html>
```